GLS biz card

We need a business card design for our new company based in Los Angeles called "Gold Lantern Studios". We develop film and television projects. We work with investors, financiers, film production companies, film distribution and sales companies as well as studios. We would like to incorporate our logo (see attached) on a two-sided card. We need to include: name and title, address, phone, email and company website.

Target Market(s)

Business, financial and studio clients

Industry/Entity Type

Business

Contact Information for Business Card

Two-sided. We are thinking of the logo on one side and the information on the back. Please feel free to be creative! Thanks.

Requirements
Must have
• Please include the following text information, excluding the "CAPS CATEGORY:" and please allow the ability for us to change the name, title and email address for each company employee):
• NAME & TITLE:
• Peter Harlow
• Managing Partner
• COMPANY NAME:
• GOLD LANTERN STUDIOS (please use existing logo)
• COMPANY ADDRESS:
• TKV Media Campus
• 2840 Welwood Avenue
• Tarlow Center, 4th Floor
• Manhattan Beach, CA 90271
• COMPANY PHONE NUMBER:
• 310-555-0148
• COMPANY WEBSITE ADDRESS:
• www.goldlanternstudiosgroup.example
• EMAIL ADDRESS: (only one per card)
• martin@goldlanternstudiosgroup.example
• buzzy@goldlanternstudiosgroup.example
• peter@goldlanternstudiosgroup.example

```html
<!DOCTYPE html>
<html lang="en">
<head>
<meta charset="utf-8">
<title>Gold Lantern Studios – Business Cards</title>
<link href="https://fonts.googleapis.com/css2?family=Questrial&display=swap" rel="stylesheet">
<style>
  :root {
    --page: #ffffff;
    --card-top: #0d1117;
    --card-bottom: #020305;
    --brand: #2aa9e0;
    --flare: #3f8dff;
    --flare-core: #d8ecff;
    --name: #c9ccd1;
    --detail: #b7bcc3;
  }
  * { box-sizing: border-box; margin: 0; padding: 0; }
  html, body { width: 1200px; height: 645px; overflow: hidden; background: var(--page); }
  body { position: relative; font-family: "Questrial", sans-serif; }

  .card {
    position: absolute;
    width: 395px;
    height: 237px;
    overflow: hidden;
    background: radial-gradient(ellipse at 50% 40%, var(--card-top) 0%, var(--card-bottom) 80%);
  }
  .card--martin { left: 155px; top: 61px; }
  .card--peter  { left: 652px; top: 61px; }
  .card--back   { left: 155px; top: 310px; }
  .card--buzzy  { left: 652px; top: 310px; }

  .brand { position: absolute; text-align: center; color: var(--brand); text-transform: uppercase; }
  .brand__dot { display: block; margin: 0 auto; border-radius: 50%; background: var(--brand); }
  .brand__name { display: block; letter-spacing: 0.14em; line-height: 1.25; }

  .card .brand { left: 28px; top: 28px; width: 112px; }
  .card .brand__dot { width: 34px; height: 34px; margin-bottom: 8px; }
  .card .brand__name { font-size: 8.5px; }

  .card--back .brand { left: 97px; top: 56px; width: 200px; }
  .card--back .brand__dot { width: 52px; height: 52px; margin-bottom: 12px; }
  .card--back .brand__name { font-size: 15px; }
  .tagline { display: block; margin-top: 6px; font-size: 6px; letter-spacing: 0.12em; color: #e6e8eb; }
  .website { position: absolute; left: 0; right: 0; top: 196px; text-align: center; font-size: 9.5px; color: var(--detail); }

  .person { position: absolute; left: 198px; top: 54px; }
  .person__name { font-size: 16px; color: var(--name); line-height: 1.1; }
  .person__title { font-size: 8.5px; color: var(--detail); margin-top: 5px; }

  .flare {
    position: absolute; left: 0; right: 0; top: 130px; height: 14px;
    background: radial-gradient(ellipse 45% 50% at 50% 50%, rgba(63,141,255,0.45) 0%, rgba(63,141,255,0) 100%);
  }
  .flare::before {
    content: ""; position: absolute; left: 0; right: 0; top: 6px; height: 1.5px;
    background: linear-gradient(90deg, rgba(63,141,255,0) 0%, var(--flare) 25%, var(--flare-core) 50%, var(--flare) 75%, rgba(63,141,255,0) 100%);
  }

  .address {
    position: absolute; left: 0; right: 0; top: 166px;
    text-align: center; font-size: 9px; line-height: 14px; color: var(--detail);
  }
</style>
</head>
<body>

  <section class="card card--martin">
    <div class="brand"><span class="brand__dot"></span><span class="brand__name">Gold Lantern<br>Studios</span></div>
    <div class="person">
      <p class="person__name">Martin Keller</p>
      <p class="person__title">Partner</p>
    </div>
    <div class="flare"></div>
    <address class="address" style="font-style:normal">
      TKV Media Campus &nbsp;||&nbsp; 2840 Welwood Avenue<br>
      Tarlow Center, 4th Floor &nbsp;||&nbsp; Manhattan Beach, CA 90271<br>
      310-555-0148 &nbsp;||&nbsp; martin@goldlanternstudiosgroup.example
    </address>
  </section>

  <section class="card card--peter">
    <div class="brand"><span class="brand__dot"></span><span class="brand__name">Gold Lantern<br>Studios</span></div>
    <div class="person">
      <p class="person__name">Peter Harlow</p>
      <p class="person__title">Partner</p>
    </div>
    <div class="flare"></div>
    <address class="address" style="font-style:normal">
      TKV Media Campus &nbsp;||&nbsp; 2840 Welwood Avenue<br>
      Tarlow Center, 4th Floor &nbsp;||&nbsp; Manhattan Beach, CA 90271<br>
      310-555-0148 &nbsp;||&nbsp; peter@goldlanternstudiosgroup.example
    </address>
  </section>

  <section class="card card--back">
    <div class="brand">
      <span class="brand__dot"></span>
      <span class="brand__name">Gold Lantern<br>Studios</span>
      <span class="tagline">A Media Entertainment Company</span>
    </div>
    <p class="website">www.goldlanternstudiosgroup.example</p>
  </section>

  <section class="card card--buzzy">
    <div class="brand"><span class="brand__dot"></span><span class="brand__name">Gold Lantern<br>Studios</span></div>
    <div class="person">
      <p class="person__name">Buzzy Carlton</p>
      <p class="person__title">President || CEO</p>
    </div>
    <div class="flare"></div>
    <address class="address" style="font-style:normal">
      TKV Media Campus &nbsp;||&nbsp; 2840 Welwood Avenue<br>
      Tarlow Center, 4th Floor &nbsp;||&nbsp; Manhattan Beach, CA 90271<br>
      310-555-0148 &nbsp;||&nbsp; buzzy@goldlanternstudiosgroup.example
    </address>
  </section>

</body>
</html>
```